Design some Business Cards for HVBA

Wording for business cards:

Company: Harbor Vessel Brokers Alliance
Name: Dominic Farrow
Job Title: Network Development Executive
email: dominic@[login to view URL]
Tel/Mob: Mobile: +001 418-275-9062
Skype: [login to view URL]
Address: 4780 SE 63rd Blvd; Ste 240, Miami FL 33058, USA
website: [login to view URL]

```html
<!DOCTYPE html>
<html lang="en">
<head>
<meta charset="utf-8">
<title>HVBA Business Cards</title>
<link href="https://fonts.googleapis.com/css2?family=Montserrat:wght@400;600;700&family=Roboto:wght@400;500&display=swap" rel="stylesheet">
<style>
  :root {
    --bg: #ece9e4;
    --card: #ffffff;
    --navy: #34358c;
    --band-top: #5b5aa9;
    --red: #e3222b;
    --ink: #1d1d24;
    --muted: #4a4a55;
  }
  * { box-sizing: border-box; margin: 0; padding: 0; }
  html, body { width: 1200px; height: 912px; overflow: hidden; }
  body { background: var(--bg); position: relative; font-family: "Roboto", Arial, sans-serif; }

  .card {
    position: absolute;
    width: 540px; height: 308px;
    background: var(--card);
    box-shadow: 0 10px 28px rgba(0,0,0,.18);
    overflow: hidden;
  }
  .card--front { left: 70px; top: 80px; }
  .card--back  { left: 590px; top: 524px; }

  .card__bands { position: absolute; inset: 0; width: 100%; height: 100%; }

  .brand { position: absolute; display: flex; align-items: center; gap: 12px; }
  .brand__dot { width: 50px; height: 50px; border-radius: 50%; background: var(--navy); flex: none; }
  .brand__text { display: flex; flex-direction: column; }
  .brand__name {
    font-family: "Montserrat", Arial, sans-serif; font-weight: 700;
    font-size: 38px; letter-spacing: 3px; color: var(--navy); line-height: 1;
  }
  .brand__rule { height: 2px; background: var(--red); margin: 4px 0 3px; }
  .brand__tagline {
    font-family: "Montserrat", Arial, sans-serif; font-weight: 700;
    font-size: 8px; letter-spacing: .4px; color: var(--navy); text-transform: uppercase;
    white-space: nowrap;
  }
  .card--front .brand { left: 118px; top: 112px; }
  .card--back .brand { left: 30px; top: 140px; }
  .card--back .brand__name { font-size: 32px; }
  .card--back .brand__dot { width: 42px; height: 42px; }
  .card--back .brand__tagline { font-size: 7.5px; }

  .website {
    position: absolute; right: 110px; bottom: 62px;
    font-size: 14px; font-weight: 500; color: var(--ink);
  }

  .contact { position: absolute; left: 292px; top: 44px; width: 232px; }
  .contact__name {
    font-family: "Montserrat", Arial, sans-serif; font-weight: 400;
    font-size: 20px; color: var(--navy); line-height: 1.1;
  }
  .contact__title { font-size: 10px; color: var(--red); margin: 3px 0 14px; }
  .contact__list { list-style: none; }
  .contact__item { display: flex; align-items: flex-start; gap: 7px; font-size: 10.5px; color: var(--muted); line-height: 1.3; margin-bottom: 4px; }
  .contact__icon { width: 11px; height: 11px; flex: none; margin-top: 1px; }
</style>
</head>
<body>

  <section class="card card--front" aria-label="Business card front">
    <svg class="card__bands" viewBox="0 0 540 308" preserveAspectRatio="none" aria-hidden="true">
      <polygon points="96,0 322,0 310,20 84,20" fill="var(--band-top)"/>
      <polygon points="0,278 290,278 272,308 0,308" fill="var(--red)"/>
      <polygon points="290,278 540,278 540,308 272,308" fill="var(--navy)"/>
    </svg>
    <div class="brand">
      <span class="brand__dot"></span>
      <div class="brand__text">
        <span class="brand__name">HVBA</span>
        <span class="brand__rule"></span>
        <span class="brand__tagline">Harbor Vessel Brokers Alliance</span>
      </div>
    </div>
    <p class="website">www.go2hvba.com</p>
  </section>

  <section class="card card--back" aria-label="Business card back">
    <svg class="card__bands" viewBox="0 0 540 308" preserveAspectRatio="none" aria-hidden="true">
      <polygon points="96,0 322,0 310,20 84,20" fill="var(--band-top)"/>
      <polygon points="0,278 290,278 272,308 0,308" fill="var(--red)"/>
      <polygon points="290,278 540,278 540,308 272,308" fill="var(--navy)"/>
    </svg>
    <div class="brand">
      <span class="brand__dot"></span>
      <div class="brand__text">
        <span class="brand__name">HVBA</span>
        <span class="brand__rule"></span>
        <span class="brand__tagline">Harbor Vessel Brokers Alliance</span>
      </div>
    </div>
    <div class="contact">
      <h1 class="contact__name">Dominic Farrow</h1>
      <p class="contact__title">Network Development Executive</p>
      <ul class="contact__list">
        <li class="contact__item">
          <svg class="contact__icon" viewBox="0 0 12 12" aria-hidden="true"><path d="M6 0.5C3.8 0.5 2.2 2.1 2.2 4.2 2.2 7 6 11.5 6 11.5S9.8 7 9.8 4.2C9.8 2.1 8.2 0.5 6 0.5Z" fill="var(--red)"/><circle cx="6" cy="4.2" r="1.4" fill="#fff"/></svg>
          <span>4780 SE 63rd Blvd; Ste 240,<br>Miami FL 33058, USA</span>
        </li>
        <li class="contact__item">
          <svg class="contact__icon" viewBox="0 0 12 12" aria-hidden="true"><circle cx="6" cy="6" r="5.5" fill="var(--red)"/></svg>
          <span>Dominic.Farrow</span>
        </li>
        <li class="contact__item">
          <svg class="contact__icon" viewBox="0 0 12 12" aria-hidden="true"><circle cx="6" cy="6" r="5.5" fill="var(--red)"/><path d="M4 3.2l1.2 1.4-.7.8c.5 1 1.2 1.7 2.1 2.1l.8-.7 1.4 1.2-.8 1c-2.4-.3-4.5-2.4-4.8-4.8z" fill="#fff"/></svg>
          <span>+001 418-275-9062</span>
        </li>
        <li class="contact__item">
          <svg class="contact__icon" viewBox="0 0 12 12" aria-hidden="true"><circle cx="6" cy="6" r="5.5" fill="var(--red)"/><rect x="3" y="4" width="6" height="4.2" fill="#fff"/><path d="M3 4l3 2.3L9 4" stroke="var(--red)" stroke-width=".8" fill="none"/></svg>
          <span>dominic@go2hvba.com</span>
        </li>
        <li class="contact__item">
          <svg class="contact__icon" viewBox="0 0 12 12" aria-hidden="true"><circle cx="6" cy="6" r="5.5" fill="var(--red)"/><circle cx="6" cy="6" r="3" fill="none" stroke="#fff" stroke-width=".8"/><path d="M3 6h6M6 3v6" stroke="#fff" stroke-width=".7"/></svg>
          <span>www.go2hvba.com</span>
        </li>
      </ul>
    </div>
  </section>

</body>
</html>
```